Banner and logo redesign for B2B website

I want a new email banner design and logo. This is for a B2B whitepaper library hosting content and resources of technology companies.https://ml.vexomarlin.net/

Target Market(s)

B2B

Industry/Entity Type

tech B2B

Number of Pages Required

1 page

Font styles to use
Sans Serif

Requirements
Must have
• A logo and email banner
Nice to have
• Similar colour pallet to what can be found on the site
Should not have
• website designs

```html
<!DOCTYPE html>
<html lang="en">
<head>
<meta charset="utf-8">
<title>Vexo Marlin – Email Banner</title>
<link href="https://fonts.googleapis.com/css2?family=Montserrat:wght@400;500;600;700&family=Ubuntu:wght@700&display=swap" rel="stylesheet">
<style>
  :root {
    --navy: #0f2a4d;
    --ink: #1c3354;
    --band: rgba(14, 40, 88, 0.88);
    --white: #ffffff;
    --brand-blue: #2f7fd8;
    --sky-light: #eef4fb;
    --sky-mid: #c4d9ee;
    --sky-deep: #7fa6d3;
    --suit: #1a356e;
  }
  html, body {
    margin: 0;
    padding: 0;
    width: 1200px;
    height: 600px;
    overflow: hidden;
    background: var(--white);
  }
  .banner {
    position: relative;
    width: 1200px;
    height: 600px;
    overflow: hidden;
    font-family: "Montserrat", sans-serif;
  }
  .hero-visual {
    position: absolute;
    inset: 0;
    background:
      radial-gradient(ellipse 260px 380px at 950px 260px, rgba(26, 53, 110, 0.85), rgba(26, 53, 110, 0) 100%),
      radial-gradient(ellipse 320px 240px at 700px 260px, rgba(140, 190, 240, 0.55), rgba(140, 190, 240, 0) 100%),
      linear-gradient(90deg, var(--sky-light) 0%, var(--sky-mid) 45%, var(--sky-deep) 68%, var(--suit) 100%);
  }
  .brand {
    position: absolute;
    left: 36px;
    top: 18px;
    display: flex;
    flex-direction: column;
    align-items: center;
    gap: 10px;
  }
  .brand-mark {
    width: 66px;
    height: 66px;
    border-radius: 50%;
    background: var(--brand-blue);
  }
  .brand-name {
    font-size: 22px;
    font-weight: 500;
    letter-spacing: 0.5px;
    color: var(--navy);
    text-transform: uppercase;
  }
  .headline {
    position: absolute;
    left: 36px;
    top: 196px;
    margin: 0;
    font-family: "Ubuntu", sans-serif;
    font-weight: 700;
    font-size: 45px;
    line-height: 53px;
    color: var(--navy);
  }
  .intro {
    position: absolute;
    left: 36px;
    top: 332px;
    width: 600px;
    margin: 0;
    font-size: 18.5px;
    line-height: 24px;
    color: var(--ink);
  }
  .contact-band {
    position: absolute;
    left: 0;
    top: 500px;
    width: 1200px;
    height: 75px;
    background: var(--band);
  }
  .contact-item {
    position: absolute;
    top: 11px;
    display: flex;
    align-items: center;
    gap: 18px;
    color: var(--white);
  }
  .contact-item.phone { left: 38px; }
  .contact-item.email { left: 326px; }
  .contact-icon { width: 34px; height: 34px; }
  .contact-label { font-size: 17px; font-weight: 400; line-height: 22px; }
  .contact-value { font-size: 17.5px; font-weight: 700; line-height: 24px; }
  .cta-button {
    position: absolute;
    left: 992px;
    top: 14px;
    width: 165px;
    height: 48px;
    border-radius: 6px;
    background: var(--white);
    color: var(--navy);
    font-size: 17px;
    font-weight: 500;
    display: flex;
    align-items: center;
    justify-content: center;
    text-decoration: none;
  }
</style>
</head>
<body>
<div class="banner">
  <div class="hero-visual" role="img" aria-label="Businessman in a navy suit holding a tablet with glowing financial charts and rising graph lines over a soft blue background"></div>

  <div class="brand">
    <div class="brand-mark"></div>
    <div class="brand-name">Vexo Marlin</div>
  </div>

  <h1 class="headline">Lorem Ipsum is simply<br>dummy text of the</h1>

  <p class="intro">Lorem Ipsum is simply dummy text of the printing and typesetting industry. Lorem Ipsum has been the industry's standard dummy text ever since the 1500s,</p>

  <div class="contact-band">
    <div class="contact-item phone">
      <svg class="contact-icon" viewBox="0 0 24 24" fill="none" stroke="#ffffff" stroke-width="1.5" stroke-linecap="round" stroke-linejoin="round">
        <path d="M5 3h3l2 5-2.5 1.5a11 11 0 0 0 7 7L16 14l5 2v3a2 2 0 0 1-2 2A17 17 0 0 1 3 5a2 2 0 0 1 2-2z"/>
        <path d="M15 3a6 6 0 0 1 6 6"/>
        <path d="M15 6.5a2.5 2.5 0 0 1 2.5 2.5"/>
      </svg>
      <div>
        <div class="contact-label">Call Us:</div>
        <div class="contact-value">1 (866) 555-0147</div>
      </div>
    </div>
    <div class="contact-item email">
      <svg class="contact-icon" viewBox="0 0 24 24" fill="none" stroke="#ffffff" stroke-width="1.5" stroke-linejoin="round">
        <rect x="2" y="5" width="20" height="14" rx="1"/>
        <path d="M2 6l10 7 10-7"/>
        <path d="M2 18l7-6M22 18l-7-6"/>
      </svg>
      <div>
        <div class="contact-label">Email Us:</div>
        <div class="contact-value">info@vexomarlin.net</div>
      </div>
    </div>
    <a class="cta-button" href="https://ml.vexomarlin.net/">CONTACT US</a>
  </div>
</div>
</body>
</html>
```